Ridgeline Build Network Inc. Letterhead

Creation of attractive and eye catching letterhead for a business start-up for the construction industry. Letterhead must relate to construction, but avoid standard hammer and tools in the design.
Updates

I forgot to add some details, sorry about that. Some pertinent info: Ph: 916-555-0148 ridgelinebuildnet.example 487 Willowmere Ave, Ste 210 Folsom, CA 95699 info@ridgelinebuildnet.example not sure if slogan should be in there" “Connecting construction professionals to create a purpose driven industry.” must be able to be used in word. Thanks!

```html
<!DOCTYPE html>
<html lang="en">
<head>
<meta charset="utf-8">
<title>Ridgeline Build Network Inc. Letterhead</title>
<link href="https://fonts.googleapis.com/css2?family=Roboto:wght@300;400&display=swap" rel="stylesheet">
<style>
  :root {
    --navy: #232a52;
    --red: #c0272d;
    --red-text: #b5121b;
    --ink: #1e2350;
    --body: #555559;
    --paper: #ffffff;
    --backdrop: #eef0f6;
  }
  * { margin: 0; padding: 0; box-sizing: border-box; }
  html, body { width: 1200px; height: 1200px; overflow: hidden; }
  body {
    background: var(--backdrop);
    font-family: "Roboto", Arial, sans-serif;
    position: relative;
  }
  .letterhead {
    position: absolute;
    left: 170px; top: 30px;
    width: 860px; height: 1140px;
    background: var(--paper);
    box-shadow: 0 0 40px rgba(30, 35, 70, 0.15);
  }
  .edge-band { position: absolute; left: 0; top: 0; width: 30px; height: 100%; background: var(--navy); }
  .corner-band { position: absolute; right: 0; top: 852px; width: 30px; height: 288px; background: var(--red); }

  .brand {
    position: absolute; left: 71px; top: 70px;
    display: flex; align-items: center; gap: 10px;
  }
  .brand-mark { width: 18px; height: 18px; background: var(--red); }
  .brand-name { font-size: 19px; font-weight: 400; color: var(--navy); letter-spacing: 0.5px; }

  .recipient-name { position: absolute; left: 71px; top: 232px; font-size: 19px; color: var(--red-text); font-weight: 400; }
  .recipient-address { position: absolute; left: 71px; top: 272px; font-size: 15px; line-height: 23px; color: #333; }
  .letter-date { position: absolute; right: 69px; top: 277px; font-size: 11px; color: #444; }

  .letter-body { position: absolute; left: 71px; top: 351px; width: 720px; }
  .letter-body p {
    font-size: 15px; line-height: 25.5px; font-weight: 300; color: var(--body);
    text-align: justify; margin-bottom: 26px;
  }

  .closing { position: absolute; left: 71px; top: 772px; font-size: 18px; font-weight: 300; color: var(--body); }
  .signature-area {
    position: absolute; left: 71px; top: 822px; width: 155px; height: 34px;
    background: linear-gradient(90deg, #e4e4e6, #f2f2f3);
  }
  .sender-name { position: absolute; left: 71px; top: 863px; font-size: 18px; color: var(--red-text); }
  .sender-title { position: absolute; left: 71px; top: 894px; font-size: 15px; font-weight: 300; color: var(--body); }

  .contact { position: absolute; right: 106px; text-align: right; font-size: 14.5px; color: var(--ink); line-height: 18px; }
  .contact-icon { position: absolute; left: 774px; width: 20px; height: 20px; }
  .contact-phone { top: 920px; }
  .contact-web { top: 974px; line-height: 20px; }
  .contact-address { top: 1029px; line-height: 21px; }
</style>
</head>
<body>
  <main class="letterhead">
    <div class="edge-band"></div>
    <div class="corner-band"></div>

    <header class="brand">
      <span class="brand-mark"></span>
      <span class="brand-name">Ridgeline Build Network</span>
    </header>

    <h2 class="recipient-name">Maren Okafor</h2>
    <address class="recipient-address" style="font-style:normal">12-4, Harlow Street,<br>Singapore 208841</address>
    <div class="letter-date">Date: 01 September, 2018</div>

    <section class="letter-body">
      <p>Lorem ipsum dolor sit amet, consectetur adipiscing elit, sed do eiusmod tempor incididunt ut labore et dolore magna aliqua. Ut enim ad minim veniam, quis nostrud exercitation ullamco laboris nisi ut aliquip ex ea commodo consequat. Duis aute irure dolor in reprehenderit in voluptate velit esse cillum dolore eu fugiat nulla pariatur. Excepteur sint occaecat cupidatat non proident, sunt in culpa qui officia deserunt mollit anim id est laborum.</p>
      <p>Lorem ipsum dolor sit amet, consectetur adipiscing elit, sed do eiusmod tempor incididunt ut labore et dolore magna aliqua. Ut enim ad minim veniam, quis nostrud exercitation ullamco laboris nisi ut aliquip ex ea commodo consequat.Duis aute irure dolor in reprehenderit in voluptate velit esse cillum dolore eu fugiat nulla pariatur. Excepteur sint occaecat cupidatat non proident, sunt in culpa qui officia deserunt mollit anim id est laborum</p>
      <p>But I must explain to you how all this mistaken idea of denouncing pleasure and praising pain was born and I will give you a complete account of the system, and expound the actual teachings of the great explorer of the truth, the master-builder of human happiness.</p>
    </section>

    <div class="closing">Regards</div>
    <div class="signature-area" role="img" aria-label="Handwritten signature of Daniel Whitcombe"></div>
    <div class="sender-name">Daniel Whitcombe</div>
    <div class="sender-title">Executive Director</div>

    <div class="contact contact-phone">916-555-0148<br>916-555-0148</div>
    <svg class="contact-icon" style="top:928px" viewBox="0 0 24 24" aria-hidden="true">
      <path fill="#b5121b" d="M6.6 10.8a15.1 15.1 0 0 0 6.6 6.6l2.2-2.2c.3-.3.7-.4 1-.2 1.1.4 2.3.6 3.6.6.6 0 1 .4 1 1V20c0 .6-.4 1-1 1A17 17 0 0 1 3 4c0-.6.4-1 1-1h3.5c.6 0 1 .4 1 1 0 1.3.2 2.5.6 3.6.1.3 0 .7-.2 1z"/>
    </svg>

    <div class="contact contact-web">info@ridgelinebuildnet.example<br>ridgelinebuildnet.example</div>
    <svg class="contact-icon" style="top:984px" viewBox="0 0 24 24" aria-hidden="true">
      <g fill="none" stroke="#b5121b" stroke-width="1.6">
        <circle cx="12" cy="12" r="10"/>
        <ellipse cx="12" cy="12" rx="4.5" ry="10"/>
        <line x1="2" y1="12" x2="22" y2="12"/>
        <path d="M4 6.5h16M4 17.5h16"/>
      </g>
    </svg>

    <div class="contact contact-address">487 Willowmere Ave, Ste 210<br>Folsom, CA 95699</div>
    <svg class="contact-icon" style="top:1040px" viewBox="0 0 24 24" aria-hidden="true">
      <path fill="#b5121b" d="M12 2a7 7 0 0 0-7 7c0 5 7 13 7 13s7-8 7-13a7 7 0 0 0-7-7zm0 9.5A2.5 2.5 0 1 1 12 6.5a2.5 2.5 0 0 1 0 5z"/>
    </svg>
  </main>
</body>
</html>
```